Demo, Strip out Rubbish and Asbestos Removal

we need a business card to give to clients to provide information about our Demo Strip out rubbish and Asbestos removal as well as labour hire.
I was thinking of a silhouette of a tip truck with the services we provide being dumped out the back in bullet form.
KB in a green colour and Refuse in a grey colour.
Greens, greys, blacks, white, silvers, matt grey. But am very open to other colour schemers and designs. I do like the tough of a matt card with gloss writing or vies versa.
We are also looking to use this design as our logo

Target Market(s)

builders - commercial residential . General public

Industry/Entity Type

Business

Contact Information for Business Card

KB Refuse
Dean Harlow
0471203658
kbrefuse@mailvista.example

Font styles to use
Sans Serif

Colors
9bcb3c
00a990
0355a3
000000
5c5c5c
cbcbcb
fbee3f
ffffff
ffcf3e

Requirements
Must have
• Abn: 57219038446
Nice to have
• bullet form
:demo and strip out
:asbestos and rubbishe removal
:labour hire
:Residential and commercial clean up
:yard clearing

```html
<!DOCTYPE html>
<html lang="en">
<head>
<meta charset="utf-8">
<title>KB Refuse – Business Card</title>
<link href="https://fonts.googleapis.com/css2?family=Source+Sans+3:wght@400;500;600&display=swap" rel="stylesheet">
<style>
  :root {
    --page: #ffffff;
    --card-black: #080908;
    --card-band: #111415;
    --lime: #9cff0a;
    --lime-soft: #c8f01e;
    --amber: #ffbf10;
    --sun: #ffcf2b;
    --ink: #ffffff;
  }
  * { margin: 0; padding: 0; box-sizing: border-box; }
  html, body {
    width: 1200px; height: 900px; overflow: hidden;
    background: var(--page);
    font-family: "Source Sans 3", "Source Sans Pro", sans-serif;
  }
  .presentation { position: relative; width: 1200px; height: 900px; }

  .card {
    position: absolute;
    overflow: hidden;
    background: var(--card-black);
    color: var(--ink);
  }
  .card-decor { position: absolute; inset: 0; width: 100%; height: 100%; }

  .card--hero  { left: 126px; top: 20px;  width: 949px; height: 558px; border-radius: 18px; }
  .card--front { left: 178px; top: 643px; width: 407px; height: 238px; border-radius: 8px; }
  .card--back  { left: 616px; top: 643px; width: 407px; height: 238px; border-radius: 8px; }

  .brand-name {
    position: absolute; left: 0; right: 0;
    text-align: center; font-weight: 500; line-height: 1;
    letter-spacing: 0.03em; white-space: nowrap;
  }
  .card--hero .brand-name  { top: 236px; font-size: 88px; }
  .card--front .brand-name { top: 102px; font-size: 37px; }

  .contact { position: absolute; left: 136px; line-height: 1; white-space: nowrap; }
  .contact-name  { top: 68px;  font-size: 24px; font-weight: 500; letter-spacing: 0.02em; }
  .contact-phone { top: 103px; font-size: 14px; letter-spacing: 0.04em; }
  .contact-email { top: 130px; font-size: 15px; letter-spacing: 0.03em; }
  .contact-abn   { top: 155px; font-size: 13px; letter-spacing: 0.04em; }
</style>
</head>
<body>
<main class="presentation">

  <svg width="0" height="0" style="position:absolute" aria-hidden="true">
    <defs>
      <linearGradient id="ribbon-glow" x1="0" y1="0" x2="1" y2="0">
        <stop offset="0" stop-color="var(--amber)" stop-opacity="0.55"/>
        <stop offset="0.5" stop-color="var(--lime-soft)" stop-opacity="0.25"/>
        <stop offset="1" stop-color="var(--lime-soft)" stop-opacity="0"/>
      </linearGradient>
    </defs>
  </svg>

  <!-- Hero view of the card front -->
  <section class="card card--hero">
    <svg class="card-decor" viewBox="0 0 949 558" aria-hidden="true">
      <rect x="0" y="417" width="949" height="141" fill="var(--card-band)"/>
      <rect x="871" y="346" width="110" height="34" rx="17" fill="var(--lime)"/>
      <rect x="871" y="383" width="110" height="34" rx="17" fill="var(--sun)"/>
    </svg>
    <svg class="card-decor" viewBox="0 0 949 558" role="img" aria-label="Flowing lime and amber ribbon decoration along the left edge">
      <rect x="0" y="0" width="145" height="455" fill="url(#ribbon-glow)"/>
    </svg>
    <h1 class="brand-name">KB Refuse</h1>
  </section>

  <!-- Card front -->
  <section class="card card--front">
    <svg class="card-decor" viewBox="0 0 949 558" aria-hidden="true">
      <rect x="0" y="417" width="949" height="141" fill="var(--card-band)"/>
      <rect x="871" y="346" width="110" height="34" rx="17" fill="var(--lime)"/>
      <rect x="871" y="383" width="110" height="34" rx="17" fill="var(--sun)"/>
    </svg>
    <svg class="card-decor" viewBox="0 0 949 558" role="img" aria-label="Flowing lime and amber ribbon decoration along the left edge">
      <rect x="0" y="0" width="145" height="455" fill="url(#ribbon-glow)"/>
    </svg>
    <h2 class="brand-name">KB Refuse</h2>
  </section>

  <!-- Card back -->
  <section class="card card--back">
    <svg class="card-decor" viewBox="0 0 949 558" aria-hidden="true">
      <rect x="0" y="417" width="949" height="141" fill="var(--card-band)"/>
      <g transform="translate(949 0) scale(-1 1)">
        <rect x="871" y="346" width="110" height="34" rx="17" fill="var(--lime)"/>
        <rect x="871" y="383" width="110" height="34" rx="17" fill="var(--sun)"/>
      </g>
    </svg>
    <svg class="card-decor" viewBox="0 0 949 558" role="img" aria-label="Flowing lime and amber ribbon decoration along the right edge">
      <g transform="translate(949 0) scale(-1 1)">
        <rect x="0" y="0" width="145" height="455" fill="url(#ribbon-glow)"/>
      </g>
    </svg>
    <p class="contact contact-name">Dean Harlow</p>
    <p class="contact contact-phone">0471203658</p>
    <p class="contact contact-email">kbrefuse@mailvista.example</p>
    <p class="contact contact-abn">ABN 57219038446</p>
  </section>

</main>
</body>
</html>
```